'Cradle Ahead' promotional brochure

We have designed a 6 week program to educate impending first-time parents about the things they need to know to survive the first 6 months. Sessions delivered by general practitioner/family doctor, dietician, physiotherapist, speech pathologist and psychologist. Our promotional blurb is: 'A comprehensive education program for first-time parents-to-be, delivered over 6 weeks by health professionals in your community, about everything you need to know to look after your baby (and yourself!) in the first 6 months'. I now want to put together a promotional brochure to be distributed to those couples who express an interest which will provide further details of what will be delivered in the course.
Updates
In terms of layout, I envisaged a double sided A4 size, foldable into 3 sections, but very happy to be guided on this.
Target Market(s)
To appeal to a young, well educated demographic. First time parents couples.
Industry/Entity Type
Medical
Font styles to use
Other font styles liked:
- Playfair Display
Requirements
Must have
- Playfair display font to be consistent with our logo (attached). Logo also included please. Some consistency with colours of logo please.
Nice to have
- I am a doctor, and have no creative genes! But prefer a clean and professional appearance overall. Not too cluttered in overall appearance.
Should not have
- No cheesy pictures of babies.

```html
<!DOCTYPE html>
<html lang="en">
<head>
<meta charset="utf-8">
<title>Cradle Ahead – Brochure</title>
<link href="https://fonts.googleapis.com/css2?family=Playfair+Display:wght@400;700;900&family=Lato:wght@400;700&display=swap" rel="stylesheet">
<style>
:root{
  --backdrop:#d1d2d4;
  --paper:#f7f7f7;
  --white:#ffffff;
  --green:#5cb946;
  --green-deep:#2f7d46;
  --grey-panel:#8d8e90;
  --grey-title:#555657;
  --ink:#4a4a4a;
  --ink-soft:#6a6a6a;
}
*{box-sizing:border-box;margin:0;padding:0}
html,body{width:879px;height:1200px;overflow:hidden}
body{background:var(--backdrop);font-family:"Lato",sans-serif;color:var(--ink);position:relative}
.spread{position:absolute;left:102px;width:690px;height:488px;display:flex;box-shadow:0 1px 3px rgba(0,0,0,.12)}
.spread--outside{top:97px}
.spread--inside{top:616px}
.panel{position:relative;width:230px;height:100%;overflow:hidden;background:var(--paper)}
.panel--white{background:var(--white)}
.photo{position:absolute;left:0;width:100%}
.week-pill{display:inline-block;background:var(--green);color:var(--white);font-family:"Playfair Display",serif;font-weight:700;font-size:16px;line-height:1;padding:2px 12px 3px;border-radius:10px;letter-spacing:.5px}
.week-pill--white{background:var(--white);color:var(--grey-panel)}
.week-pill--white-green{background:var(--white);color:var(--green)}
.session{font-size:8.2px;line-height:1.33;text-align:justify;color:var(--ink)}
.session b{display:block;font-weight:700;color:var(--ink);margin-bottom:1px}
.session+.session{margin-top:10px}
.block{position:absolute;left:20px;right:20px}
.logo-name{font-family:"Playfair Display",serif;font-weight:400;color:var(--green);line-height:1.05;text-transform:uppercase;display:flex;align-items:center;gap:10px}
.logo-name .dot{width:28px;height:28px;border-radius:50%;background:var(--green);flex:none}
.bullets{list-style:none;font-size:8.4px;line-height:1.75}
.bullets li::before{content:"•";margin-right:6px}
.bullets--green li::before{color:var(--green)}
/* outside */
.contact-card{position:absolute;left:17px;top:18px;width:197px;height:452px;background:linear-gradient(160deg,#3e8a50 0%,#2f7d46 55%,#3a8b4c 100%)}
.contact-card .logo-name{color:var(--white);position:absolute;left:34px;top:188px;font-size:12px}
.contact-card .logo-name .dot{background:var(--white);width:24px;height:24px}
.contact-list{position:absolute;left:0;right:0;top:242px;text-align:center;color:var(--white);font-size:7.4px;line-height:1.3}
.contact-list .item{margin-bottom:9px}
.contact-list svg{display:block;margin:0 auto 3px}
.web-pill{position:absolute;left:18px;right:18px;top:410px;height:16px;border-radius:8px;background:var(--white);color:var(--green-deep);font-size:7px;font-weight:700;text-align:center;line-height:16px}
.cover-logo{position:absolute;left:40px;top:28px;font-size:14px}
.cover-url{position:absolute;left:0;right:0;top:90px;text-align:center;font-size:7.4px;color:var(--ink-soft)}
.cover-title{position:absolute;left:0;right:0;top:330px;text-align:center;font-family:"Playfair Display",serif;font-weight:900;font-size:36px;line-height:.9;color:var(--grey-title)}
.cover-title span{display:block;color:var(--green)}
.cover-sub{position:absolute;left:0;right:0;top:412px;text-align:center}
.cover-sub .week-pill{font-size:15px;padding:2px 14px}
.cover-sub p{font-family:"Playfair Display",serif;color:var(--grey-title);font-size:14px;line-height:1.1;margin-top:3px}
.cover-sub p+p{font-size:12px;margin-top:1px;color:var(--ink)}
/* inside */
.intro{position:absolute;left:0;top:0;width:100%;height:222px;background:var(--grey-panel);color:var(--white)}
.intro h1{font-family:"Playfair Display",serif;font-weight:900;font-size:34px;line-height:.92;text-align:center;margin-top:34px}
.intro p{font-family:"Playfair Display",serif;font-size:9.2px;line-height:1.42;text-align:justify;margin:20px 20px 0 26px}
.intro p b{font-weight:700}
.inside-logo{position:absolute;left:40px;top:408px;font-size:14px}
.week1{position:absolute;left:0;top:0;width:100%;height:222px;background:linear-gradient(135deg,#3f7f4c,#2c6e3f 60%,#3b8a4e);color:var(--white)}
.week1 .inner{position:absolute;left:22px;right:18px;top:42px}
.week1 p{font-size:8.4px;line-height:1.35;margin-top:10px}
.week1 .bullets{margin-top:5px;margin-left:10px}
.week2{position:absolute;left:0;top:222px;width:100%;height:266px;background:var(--grey-panel);color:var(--white)}
.week2 .inner{position:absolute;left:22px;right:18px;top:35px}
.week2 .session,.week2 .session b{color:var(--white)}
.week2 .week-pill{margin-bottom:12px}
.week3{top:26px}
.week3 .week-pill,.week4 .week-pill{margin-bottom:10px}
.week4{top:274px}
.week4 .bullets{margin-top:10px;margin-left:6px;color:var(--ink)}
</style>
</head>
<body>

<section class="spread spread--outside">
  <article class="panel panel--white">
    <div class="photo" style="top:0;height:158px;background:linear-gradient(180deg,#d9d3b8 0%,#c8bb8c 55%,#8f8a4c 100%)" role="img" aria-label="Couple in a sunny meadow holding hands"></div>
    <div class="block" style="top:182px">
      <span class="week-pill">WEEK 5</span>
      <div class="session" style="margin-top:10px"><b>SESSION 1</b>Clinical Psychologist Dr Maren Holt will share information about bonding &amp; attachment with your baby, how to promote their social &amp; emotional development and how to manage separation anxiety. She will also discuss positive parenting approaches.</div>
    </div>
    <div class="block" style="top:307px">
      <span class="week-pill">WEEK 6</span>
      <div class="session" style="margin-top:10px"><b>SESSION 1</b>Secret Men's Business – a men-only session (including beer!) with a new father for frank discussion about the road ahead. Mums will do a shopping excursion with the GP &amp; Dietician to Greenleaf Grocers to look at baby products and food – the good and the bad!</div>
      <div class="session"><b>SESSION 2</b>Program review, reflection and evaluation and future session planning when baby is 6 months of age.</div>
    </div>
  </article>

  <article class="panel">
    <div class="contact-card" role="img" aria-label="Expectant mother cradling her belly, green tinted photograph">
      <div class="logo-name"><span class="dot"></span><span>Wattlebrook<br>Health &amp;<br>Medical</span></div>
      <div class="contact-list">
        <div class="item">
          <svg width="10" height="12" viewBox="0 0 10 12"><path d="M5 0a4.5 4.5 0 0 0-4.5 4.5C.5 8 5 12 5 12s4.5-4 4.5-7.5A4.5 4.5 0 0 0 5 0z" fill="#fff"/><circle cx="5" cy="4.5" r="1.7" fill="#2f7d46"/></svg>
          Wattlebrook Village, Shop 7<br>219 Wattlebrook Way<br>Wattlebrook NSW 2519
        </div>
        <div class="item">
          <svg width="11" height="11" viewBox="0 0 11 11"><circle cx="5.5" cy="5.5" r="5.5" fill="#fff"/><path d="M3.6 2.8l1 1.2-.5.8c.4.8 1 1.4 1.8 1.8l.8-.5 1.2 1-.6 1c-2.3-.3-4.2-2.2-4.5-4.5z" fill="#2f7d46"/></svg>
          02 5550 0188
        </div>
        <div class="item" style="margin-top:14px">
          <svg width="11" height="11" viewBox="0 0 11 11"><circle cx="5.5" cy="5.5" r="5.5" fill="#fff"/><rect x="3" y="4" width="5" height="3.5" fill="#2f7d46"/><rect x="3.8" y="2.6" width="3.4" height="1.4" fill="#2f7d46"/></svg>
          02 5550 0199
        </div>
        <div class="item" style="margin-top:14px">
          <svg width="11" height="11" viewBox="0 0 11 11"><circle cx="5.5" cy="5.5" r="5.5" fill="#fff"/><rect x="2.8" y="3.6" width="5.4" height="3.8" fill="#2f7d46"/><path d="M2.8 3.6l2.7 2 2.7-2" stroke="#fff" stroke-width=".6" fill="none"/></svg>
          hello@wattlebrookhealth.com.au
        </div>
      </div>
      <div class="web-pill">www.wattlebrookhealth.com.au</div>
    </div>
  </article>

  <article class="panel">
    <div class="logo-name cover-logo"><span class="dot"></span><span>Wattlebrook<br>Health &amp;<br>Medical</span></div>
    <div class="cover-url">www.wattlebrookhealth.com.au</div>
    <svg style="position:absolute;left:13px;top:122px" width="206" height="180" viewBox="0 0 206 180" role="img" aria-label="Hands forming a heart over a pregnant belly">
      <defs><linearGradient id="heartTone" x1="0" y1="0" x2="1" y2="1"><stop offset="0" stop-color="#e8c9b8"/><stop offset=".6" stop-color="#c99783"/><stop offset="1" stop-color="#a87060"/></linearGradient></defs>
      <path d="M103 180C60 140 0 105 0 52 0 20 24 0 52 0c22 0 40 12 51 30C114 12 132 0 154 0c28 0 52 20 52 52 0 53-60 88-103 128z" fill="url(#heartTone)"/>
    </svg>
    <h2 class="cover-title">CRADLE<span>AHEAD</span></h2>
    <div class="cover-sub">
      <span class="week-pill">6 WEEKS</span>
      <p>Educational Program</p>
      <p>For First Time Parents</p>
    </div>
  </article>
</section>

<section class="spread spread--inside">
  <article class="panel panel--white">
    <div class="intro">
      <h1>CRADLE<br>AHEAD</h1>
      <p>A comprehensive <b>education program</b> for first-time parents-to-be, delivered <b>over 6 weeks by health professionals</b> in your community, about everything you need to know to look after your baby (and yourself!) in the first 6 months.</p>
    </div>
    <div class="photo" style="top:222px;height:153px;background:linear-gradient(135deg,#e7cdb8 0%,#f1e2d2 45%,#b9cf8a 100%)" role="img" aria-label="Parent's hand holding a sleeping newborn's hand"></div>
    <div class="logo-name inside-logo"><span class="dot"></span><span>Wattlebrook<br>Health &amp;<br>Medical</span></div>
  </article>

  <article class="panel">
    <div class="week1" role="img" aria-label="Couple embracing the pregnant belly, green tinted photograph">
      <div class="inner">
        <span class="week-pill week-pill--white-green">WEEK 1</span>
        <p>GP Dr Ilse Varga will share information for Mum's own health after delivery.<br><b>Topics include:</b></p>
        <ul class="bullets">
          <li>Vaccinations in pregnancy</li>
          <li>Bleeding, bladder and bowel after delivery</li>
          <li>Breastfeeding, engorgement and mastitis</li>
          <li>Bottle feeding</li>
          <li>Post-natal anxiety &amp; depression</li>
          <li>Intimacy and contraception</li>
        </ul>
      </div>
    </div>
    <div class="week2">
      <div class="inner">
        <span class="week-pill week-pill--white">WEEK 2</span>
        <div class="session"><b>SESSION 1</b>Clinical Psychologist Dr Maren Holt will discuss changes in relationships as couples becomes parents, gender roles in parenting and post-natal depression.</div>
        <div class="session"><b>SESSION 2</b>Physiotherapist Tess Calloway will present advice for Mums regarding exercise during and after pregnancy, looking after the pelvic floor during and after pregnancy, and abdominal muscle separation management. She will also provide advice for promoting babies' neck strength and minimising the risk of flat spots on the head and encouraging gross motor skills in the first 6 months</div>
      </div>
    </div>
  </article>

  <article class="panel panel--white">
    <div class="block week3">
      <span class="week-pill">WEEK 3</span>
      <div class="session"><b>SESSION 1</b>Dietician Nora Beckett provides advice for Mums regarding healthy eating during pregnancy and lactation, normal weight gain during pregnancy and realistic weight loss after. She will also discuss the evidence regarding breastfeeding VS bottle-feeding, normal infant weight gain and introducing solids (including those with potential for allergy).</div>
      <div class="session"><b>SESSION 2</b>Paediatric Speech Pathologist Ruth Ambrose will share information about latching and breast-feeding troubles &amp; tongue tie, advice about dummies and finger-sucking, introducing solids &amp; feeding (including 'pouch' food), encouraging language development and current evidence about electronic devices impacting language development.</div>
    </div>
    <div class="block week4">
      <span class="week-pill">WEEK 4</span>
      <div class="session">GP Dr Ilse Varga will share advice about your babies' health in the first 6 months, including:</div>
      <ul class="bullets bullets--green">
        <li>Skin of newborns</li>
        <li>Sleeping</li>
        <li>Crying</li>
        <li>Immunisations</li>
        <li>Fever and infections</li>
        <li>Diarrhoea and constipation</li>
        <li>Teething</li>
        <li>Understanding a baby's signals</li>
      </ul>
    </div>
  </article>
</section>

</body>
</html>
```